TARPLOAD business card design

TARPLOAD is a manufacturer of skip bags supplying both the domestic and commercial market. We wish to convey core characteristics of strength, professionalism and reliability to our customers. We are after a business card that uses our company colours of black and yellow as well as incorporating our logo. Our customers are predominantly in the construction or hardware industry. It is important the cards are professional as we are a small company wishing to appear larger than we actually are. more info on the company and product available at www.tarpload-example.com.au

Target Market(s)

hardware buyers, contruction company owners

Industry/Entity Type

Construction

Requirements
Must have
• company colours of black and yellow - No other colours or variation of yellow black. our company logo. card design must convey "tough"
• Card design must be landscape
• Details to be included on the card are:
• Name and Tiltle
• Phone number : 1300 41 62 53
• Mobile: 0452 718 903
• Fax: 03 9617 4852
• email: dale.hendry@tarpload-example.com.au
• address: PO Box 517, Kelvindale, VIC,3294
• Text in white when on a black background
Nice to have
• I like the idea of the back of the card being black with lighter circle area in the middle with black logo in the centre. Similar to the attached "iconic" card

```html
<!DOCTYPE html>
<html lang="en">
<head>
<meta charset="utf-8">
<title>TARPLOAD business card</title>
<link rel="stylesheet" href="https://fonts.googleapis.com/css2?family=Arimo:wght@700&family=Questrial&display=swap">
<style>
  :root {
    --bg: #dcdcdc;
    --yellow: #e3a021;
    --black: #0c0c0c;
    --band: #1d1d1d;
    --panel: #363636;
    --white: #f2f2f2;
    --label: #5e5e5e;
    --muted: #bdbdbd;
  }
  * { box-sizing: border-box; margin: 0; padding: 0; }
  html, body {
    width: 1197px; height: 1200px; overflow: hidden;
    background: var(--bg);
  }
  .canvas {
    position: relative; width: 1197px; height: 1200px;
  }
  .card {
    position: absolute; left: 148px; width: 900px; height: 514px;
    box-shadow: 0 6px 18px rgba(0,0,0,0.35);
    overflow: hidden;
  }
  /* Front */
  .card--front {
    top: 57px;
    background: radial-gradient(circle at 50% 42%, #4a3a12 0%, #1c170b 30%, var(--black) 62%);
    display: flex; flex-direction: column; align-items: center; justify-content: center;
  }
  .front-mark {
    display: flex; align-items: center; gap: 22px;
  }
  .front-mark__square {
    width: 54px; height: 54px; background: var(--yellow);
  }
  .front-mark__name {
    font-family: "Arimo", Arial, sans-serif; font-weight: 700;
    font-size: 96px; letter-spacing: 2px; color: var(--yellow); line-height: 1;
  }
  .front-tagline {
    margin-top: 22px;
    font-family: "Arimo", Arial, sans-serif; font-weight: 700;
    font-size: 30px; letter-spacing: 1px; color: var(--yellow);
  }
  /* Back */
  .card--back {
    top: 629px; background: var(--panel);
  }
  .back-band {
    position: absolute; left: 0; top: 0; width: 100%; height: 252px;
    background: var(--band);
    text-align: right; padding: 64px 56px 0 0;
  }
  .back-band__name {
    font-family: "Arimo", Arial, sans-serif; font-weight: 700;
    font-size: 112px; line-height: 1; letter-spacing: 2px; color: var(--yellow);
  }
  .back-band__tagline {
    margin-top: 10px;
    font-family: "Arimo", Arial, sans-serif; font-weight: 700;
    font-size: 34px; letter-spacing: 1px; color: var(--yellow);
  }
  .contact {
    position: absolute; left: 92px; top: 306px;
    font-family: "Questrial", "Century Gothic", sans-serif; color: var(--white);
  }
  .contact__row { display: flex; gap: 10px; align-items: baseline; }
  .contact__row--main { font-size: 25px; line-height: 40px; }
  .contact__row--small { font-size: 15px; line-height: 28px; color: var(--muted); }
  .contact__gap { height: 12px; }
  .contact__label { color: var(--label); }
  .person {
    position: absolute; right: 80px; top: 390px; text-align: left;
    font-family: "Questrial", "Century Gothic", sans-serif;
  }
  .person__name { font-size: 56px; line-height: 1; color: var(--muted); }
  .person__first { color: var(--white); font-weight: 700; }
  .person__title {
    font-size: 20px; letter-spacing: 4px; color: var(--muted); margin-top: 2px;
  }
</style>
</head>
<body>
<main class="canvas">
  <section class="card card--front" aria-label="Card front">
    <div class="front-mark">
      <span class="front-mark__square"></span>
      <span class="front-mark__name">TARPLOAD</span>
    </div>
    <p class="front-tagline">TOUGH BAGS, BIG LOADS</p>
  </section>

  <section class="card card--back" aria-label="Card back">
    <header class="back-band">
      <h1 class="back-band__name">TARPLOAD</h1>
      <p class="back-band__tagline">TOUGH BAGS, BIG LOADS</p>
    </header>
    <div class="contact">
      <p class="contact__row contact__row--main"><span class="contact__label">P:</span><span>1300 41 62 53</span></p>
      <p class="contact__row contact__row--main"><span class="contact__label">M:</span><span>0452 718 903</span></p>
      <p class="contact__row contact__row--main"><span class="contact__label">F:</span><span>03 9617 4852</span></p>
      <div class="contact__gap"></div>
      <p class="contact__row contact__row--small"><span class="contact__label">E:</span><span>dale.hendry@tarpload-example.com.au</span></p>
      <p class="contact__row contact__row--small"><span class="contact__label">A:</span><span>PO Box 517, Kelvindale, VIC,3294</span></p>
    </div>
    <div class="person">
      <p class="person__name"><span class="person__first">Dale</span>Hendry</p>
      <p class="person__title">managing director</p>
    </div>
  </section>
</main>
</body>
</html>
```